Digital Marketing Agency Business Card Design Project

We are a boutique marketing agency that provides premium digital marketing services that invlude
- strategic marketing plans
- Vexora Bidlines advertising
- Search engine optimization
- Digital business analytics
- Digital merketing consulting
Business card must have a premium look that makes c clear statement. We provide digital marketing services for multiple languages.

Business card on the back side should have a slogan. Boutique digital marketing.

We always go the extra mile by every project so that clients gep premium solution and 100% satisfaction.

Please design a business card that is one of a kind..

Thank you.

Psd logo uploaded and brief updated.

Target Market(s)

Companies that need strategic online presence that is reached with boutique digital marketing services in all verticals.

Industry/Entity Type

Marketing

Font styles to use
Sans Serif

Requirements
Must have
• Premium and prestigious look.
Nice to have
• Design unique business card that fits with provided logo.
Logo should include:
Tel., E-mail, web address
Business title: one is CEO, second is COO.
Business address.

Try designing dark and light version, dark with the grey-silver from the logo and light just white background with some abstract curves in blue or green.
Should not have
• No old-style design and font
No need to list our services on the business card.

```html
<!DOCTYPE html>
<html lang="en">
<head>
<meta charset="utf-8">
<title>Lumero Business Card</title>
<link href="https://fonts.googleapis.com/css2?family=Lato:wght@300;400;700;900&display=swap" rel="stylesheet">
<style>
  :root {
    --page-bg: #ece9e4;
    --blue-light: #3fd3f3;
    --blue-deep: #1aa6dc;
    --green-light: #b4dc4a;
    --green-deep: #8fc226;
    --green-band: #a6d12f;
    --name-yellow: #f4e63c;
    --ink-dark: #1d3340;
    --ink-grey: #6f7c84;
    --white: #ffffff;
  }
  * { box-sizing: border-box; margin: 0; padding: 0; }
  html, body {
    width: 1200px; height: 1023px; overflow: hidden;
    background: var(--page-bg);
    font-family: "Lato", sans-serif;
  }
  .sheet {
    width: 1200px; height: 1023px;
    display: flex; flex-direction: column; align-items: center; justify-content: center;
    gap: 40px;
  }
  .card {
    position: relative; width: 820px; height: 469px;
    border-radius: 26px; overflow: hidden;
    box-shadow: 0 10px 24px rgba(0,0,0,0.18);
  }
  /* Front */
  .card-front {
    background: linear-gradient(160deg, var(--blue-light) 0%, var(--blue-deep) 100%);
  }
  .front-art { position: absolute; inset: 0; }
  .brand {
    position: absolute; display: flex; align-items: center; gap: 16px;
  }
  .brand-dot {
    width: 58px; height: 58px; border-radius: 50%;
    border: 4px solid var(--ink-grey);
  }
  .brand-name {
    font-weight: 300; font-size: 48px; letter-spacing: 6px; color: var(--ink-grey);
  }
  .card-front .brand { left: 62px; top: 170px; }
  .contact-list {
    position: absolute; left: 62px; top: 285px; list-style: none;
    font-size: 19px; color: var(--ink-dark); line-height: 29px;
  }
  .contact-list li { display: flex; align-items: center; gap: 12px; }
  .contact-list svg { width: 16px; height: 16px; flex: none; }
  .person {
    position: absolute; right: 58px; top: 46px; text-align: right;
  }
  .person-name { font-weight: 900; font-size: 30px; color: var(--name-yellow); }
  .person-title { font-size: 19px; color: var(--ink-dark); margin-top: 2px; }
  .address {
    position: absolute; right: 58px; top: 168px; text-align: right;
    font-size: 21px; line-height: 28px; color: var(--ink-dark);
  }
  /* Back */
  .card-back {
    background: radial-gradient(ellipse at 30% 25%, var(--green-light) 0%, var(--green-deep) 80%);
  }
  .card-back .brand { left: 62px; top: 56px; }
  .card-back .brand-dot { border-color: var(--ink-grey); }
  .slogan {
    position: absolute; left: 62px; top: 160px;
    font-weight: 700; font-size: 28px; color: var(--white);
  }
  .service-list {
    position: absolute; left: 62px; top: 210px; list-style: none;
    font-size: 19px; line-height: 28px; color: var(--white);
  }
  .service-list li::before { content: "- "; }
</style>
</head>
<body>
<main class="sheet">

  <section class="card card-front" aria-label="Business card front">
    <svg class="front-art" viewBox="0 0 820 469" aria-hidden="true">
      <path d="M0 469 V395 H430 Q445 395 448 410 V430 Q450 440 462 440 H820 V469 Z" fill="var(--green-band)"/>
      <path d="M150 90 Q400 40 640 80" fill="none" stroke="rgba(255,255,255,0.25)" stroke-width="2"/>
      <path d="M380 118 L610 112" stroke="#8aa3ad" stroke-width="2"/>
      <path d="M120 460 Q260 370 400 400" fill="none" stroke="rgba(255,255,255,0.25)" stroke-width="2"/>
    </svg>

    <div class="brand">
      <span class="brand-dot"></span>
      <span class="brand-name">LUMERO</span>
    </div>

    <ul class="contact-list">
      <li><svg viewBox="0 0 16 16"><rect x="2" y="1" width="12" height="14" rx="2" fill="var(--name-yellow)"/></svg>210 486 931</li>
      <li><svg viewBox="0 0 16 16"><path d="M4 1 L7 4 L5 6 Q7 10 10 11 L12 9 L15 12 L12 15 Q3 13 1 4 Z" fill="var(--name-yellow)"/></svg>310 752 604</li>
      <li><svg viewBox="0 0 16 16"><rect x="1" y="3" width="14" height="10" fill="var(--name-yellow)"/><path d="M1 3 L8 9 L15 3" fill="none" stroke="var(--blue-deep)" stroke-width="1.5"/></svg>darla@lumeroweb.com</li>
      <li><svg viewBox="0 0 16 16"><rect x="1.5" y="1.5" width="13" height="13" fill="none" stroke="var(--name-yellow)" stroke-width="2"/></svg>www.lumeroweb.com</li>
    </ul>

    <div class="person">
      <p class="person-name">Darla Quinby</p>
      <p class="person-title">Director</p>
    </div>

    <p class="address">Your Home or Business<br>Address Here</p>
  </section>

  <section class="card card-back" aria-label="Business card back">
    <div class="brand">
      <span class="brand-dot"></span>
      <span class="brand-name">LUMERO</span>
    </div>
    <p class="slogan">Boutique Digital Marketing</p>
    <ul class="service-list">
      <li>strategic marketing plans</li>
      <li>Vexora Bidlines advertising</li>
      <li>Search engine optimization</li>
      <li>Digital business analytics</li>
    </ul>
  </section>

</main>
</body>
</html>
```